Mesa VerdaLighting and Design Web Page

We are a Sales Agency that represents 40+ LED Lighting manufacturers primarily in new commercial, industrial and architectural construction projects. We also are active in the Re-Light and Retrofit Lighting market.
Our current web page can be found at www.mesaverdalighting.example. Our local competitors are www.beaconlumenpw.example,. We would like a more dynamic website that will list our manufacturers we represent and links to their websites. Please offer suggestions to provide a more dynamic website using our new logo which is attached. Please use the color scheme from logo. The final design should communicate innovation and expertise in LED lighting.

Target Market(s)

Architects, Lighting designers, Electrical Engineers, Electrical Contractors, Electrical Distributors, Facility Engineers, Energy Engineers

Industry/Entity Type

Construction

Number of Pages Required

5+ page

Font styles to use
Other font styles liked:
• MS Reference Sans Serif, or close to our LOGO font.

Colors
f78f20
959595

Requirements
Must have
• Logo incorporated with matching background, clean professional look based on logo, links to our manufacturers web page
Nice to have
• LED Lighting project stock photos as examples
Should not have
• crowded pages with text

```html
<!DOCTYPE html>
<html lang="en">
<head>
<meta charset="utf-8">
<title>Mesa Verda Lighting and Design</title>
<link href="https://fonts.googleapis.com/css2?family=Montserrat:wght@600;700&family=Open+Sans:wght@400;600;700&display=swap" rel="stylesheet">
<style>
:root{
  --orange:#f7901e;
  --grey:#959595;
  --text:#7a7a7a;
  --heading:#4f4f4f;
  --light:#f5f5f5;
  --white:#ffffff;
}
*{box-sizing:border-box;margin:0;padding:0}
html,body{width:1200px;height:3600px;overflow:hidden}
body{font-family:"Open Sans",Arial,sans-serif;color:var(--text);background:var(--white);position:relative}
.wrap{width:1000px;margin:0 auto;position:relative}

/* header */
.site-header{height:140px;display:flex;align-items:center}
.site-header .wrap{display:flex;align-items:center;justify-content:space-between}
.brand{display:flex;align-items:center;gap:14px}
.brand-dot{width:60px;height:60px;border-radius:50%;background:var(--orange)}
.brand-name{font-weight:700;font-size:22px;color:var(--orange);white-space:nowrap}
.main-nav{display:flex;gap:28px;font-size:12px;text-transform:uppercase;color:#555}
.main-nav a{color:inherit;text-decoration:none}
.main-nav .active{color:var(--orange)}

/* hero */
.hero{position:relative;height:592px;overflow:hidden}
.hero-photo{position:absolute;inset:0;background:radial-gradient(ellipse at 72% 35%,#c0306e 0,#5a1d3a 22%,transparent 45%),linear-gradient(180deg,#140d0a 0,#3a2312 45%,#b07a3c 80%,#e6b26a 100%)}
.hero-content{position:absolute;left:100px;top:118px;width:720px;color:var(--white)}
.hero-title{font-family:"Montserrat",Arial,sans-serif;font-weight:700;font-size:44px;letter-spacing:1px;white-space:nowrap;line-height:56px}
.hero-text{font-size:15px;line-height:26px;margin-top:10px;width:560px}
.btn{display:inline-block;background:var(--orange);color:var(--white);text-transform:uppercase;font-weight:600;text-decoration:none}
.hero .btn{margin-top:22px;padding:13px 22px;font-size:19px;font-family:"Montserrat",Arial,sans-serif}
.hero-arrows{position:absolute;left:100px;top:356px;display:flex;gap:6px}
.hero-arrows span{width:32px;height:32px;border-radius:50%;background:rgba(0,0,0,.55);display:flex;align-items:center;justify-content:center}
.hero-wave{position:absolute;left:0;bottom:0;width:1200px;height:90px}

/* sections */
.section-title{font-weight:600;font-size:38px;color:var(--heading);text-align:center}
.welcome{height:432px;padding-top:40px;text-align:center}
.welcome p{font-size:13.5px;line-height:24px;width:860px;margin:18px auto 0}
.welcome .btn{margin-top:42px;padding:16px 22px;font-size:14px}

.services{height:547px;background:var(--light);padding-top:45px}
.service-list{display:flex;justify-content:space-between;margin-top:52px}
.service{width:300px;text-align:center}
.service-icon{width:150px;height:150px;border-radius:50%;background:var(--orange);border:5px solid var(--white);box-shadow:0 0 0 3px var(--orange);margin:0 auto;display:flex;align-items:center;justify-content:center}
.service h3{font-weight:400;font-size:16px;color:var(--orange);margin-top:24px;text-transform:uppercase}
.service p{font-size:13px;line-height:21px;margin-top:6px;padding:0 10px}
.btn-outline{display:inline-block;margin-top:16px;border:2px solid var(--orange);color:var(--orange);font-size:13px;padding:7px 20px;text-transform:uppercase;text-decoration:none}

.projects{height:612px;padding-top:55px}
.slider-nav{position:absolute;right:0;top:0;display:flex;gap:6px}
.slider-nav span{width:26px;height:26px;border:1px solid #bbb;display:flex;align-items:center;justify-content:center}
.project-list{display:flex;justify-content:space-between;margin-top:48px}
.project{width:315px}
.project-photo{height:178px;border:6px solid var(--white);box-shadow:0 0 0 1px #ddd}
.project h3{font-weight:700;font-size:16px;color:var(--orange);margin-top:28px;text-transform:uppercase;white-space:nowrap}
.project p{font-size:13px;line-height:22px;margin-top:12px}
.project .btn{margin-top:22px;padding:10px 18px;font-size:13px;text-transform:none}

.gallery-head{height:149px;background:var(--light);padding-top:56px}
.gallery{display:grid;grid-template-columns:repeat(4,300px);grid-template-rows:repeat(2,186px);height:372px}

.clients{height:413px;padding-top:50px;text-align:center;background:var(--light)}
.clients p{font-size:13.5px;line-height:24px;width:880px;margin:20px auto 0}
.client-row{display:flex;justify-content:center;align-items:center;gap:22px;margin-top:36px}
.client{width:170px;height:96px;background:var(--white);border:1px solid #ddd;transform:skewX(-10deg);display:flex;align-items:center;justify-content:center}
.client span{transform:skewX(10deg);font-weight:700;font-size:17px;color:#333}
.client-arrow{width:24px;height:40px}

.site-footer{height:343px;background:var(--orange);color:var(--white);padding-top:52px}
.footer-cols{display:flex}
.footer-col h4{font-weight:400;font-size:16px;text-transform:uppercase;margin-bottom:18px}
.footer-col li{list-style:none;font-size:13.5px;line-height:32px}
.footer-note{font-size:13.5px;line-height:32px}
.col-links{width:310px}
.col-contact{width:365px}
.contact-item{display:flex;align-items:center;gap:10px}
.signup{display:flex;margin-top:14px}
.signup input{width:220px;height:38px;border:0;padding:0 12px;font-family:inherit;font-size:13px;color:#aaa}
.signup button{height:38px;width:105px;border:0;background:#111;color:var(--white);font-family:inherit;font-size:13px;text-transform:uppercase}
.social{display:flex;gap:12px;margin-top:20px}
.social span{width:34px;height:34px;border-radius:50%;background:var(--white)}
.footer-bottom{border-top:1px solid rgba(255,255,255,.5);margin-top:34px;padding-top:20px;font-size:12px}
</style>
</head>
<body>

<header class="site-header">
  <div class="wrap">
    <div class="brand">
      <div class="brand-dot"></div>
      <div class="brand-name">Mesa Verda Lighting</div>
    </div>
    <nav class="main-nav">
      <a class="active" href="#">Home</a><a href="#">About</a><a href="#">Line Card</a><a href="#">Services</a><a href="#">Territory Map</a><a href="#">Photo Gallery</a><a href="#">Blog</a><a href="#">Contact</a>
    </nav>
  </div>
</header>

<section class="hero">
  <div class="hero-photo" role="img" aria-label="Night photo of a lit pedestrian bridge leading to a building with pink facade lighting"></div>
  <div class="hero-content">
    <h1 class="hero-title">MESA VERDA LIGHTING</h1>
    <p class="hero-text">Our experienced in a variety of architectural, commercial, industrial, institutional, and residential lighting projects as well as controls projects.</p>
    <a class="btn" href="#">Get Started Now</a>
  </div>
  <div class="hero-arrows">
    <span><svg width="12" height="12" viewBox="0 0 12 12"><path d="M8 1 3 6l5 5" stroke="#fff" stroke-width="2" fill="none"/></svg></span>
    <span><svg width="12" height="12" viewBox="0 0 12 12"><path d="M4 1l5 5-5 5" stroke="#fff" stroke-width="2" fill="none"/></svg></span>
  </div>
  <svg class="hero-wave" viewBox="0 0 1200 90" preserveAspectRatio="none"><path d="M0 20 Q600 120 1200 20 L1200 90 L0 90Z" fill="#fff"/></svg>
</section>

<section class="welcome">
  <h2 class="section-title">Welcome to Mesa Verda Lighting</h2>
  <p>Mesa Verda Lighting was established in 1996 and is the leading lighting and controls agency in the region servicing West Texas, New Mexico, and Mexico (Country).</p>
  <p>We are a team of experienced and talented individuals who share the same passion; "Exceed customer and manufacturer expectations by providing high-quality technical support and the best in class customer service", experts in LED Lighting systems for architectural, commercial, industrial, institutional and residential purposes as well as controls projects.</p>
  <a class="btn" href="#">Read More Information</a>
</section>

<section class="services">
  <div class="wrap">
    <h2 class="section-title">Our Services</h2>
    <div class="service-list">
      <div class="service">
        <div class="service-icon"><svg width="70" height="70" viewBox="0 0 70 70" fill="none" stroke="#fff" stroke-width="3"><rect x="14" y="18" width="22" height="44"/><rect x="36" y="32" width="20" height="30"/><path d="M20 26h10M20 36h10M20 46h10M42 40h8M42 50h8M6 62h58"/></svg></div>
        <h3>Commercial Construction</h3>
        <p>We are an integrated team of dedicated professionals ready to support your projects in English and Spanish.</p>
        <a class="btn-outline" href="#">Read More</a>
      </div>
      <div class="service">
        <div class="service-icon"><svg width="70" height="70" viewBox="0 0 70 70" fill="none" stroke="#fff" stroke-width="3"><path d="M8 62V36l14 8v-8l14 8v-8l14 8V14h10v48Z"/><path d="M18 52h6M32 52h6M46 52h6"/></svg></div>
        <h3>Industrial Construction</h3>
        <p>We are an integrated team of dedicated professionals ready to support your projects in English and Spanish.</p>
        <a class="btn-outline" href="#">Read More</a>
      </div>
      <div class="service">
        <div class="service-icon"><svg width="70" height="70" viewBox="0 0 70 70" fill="none" stroke="#fff" stroke-width="3"><rect x="10" y="10" width="50" height="50"/><path d="M18 52 52 18M18 52V30M18 52h22"/></svg></div>
        <h3>Architectural Construction</h3>
        <p>We are an integrated team of dedicated professionals ready to support your projects in English and Spanish.</p>
        <a class="btn-outline" href="#">Read More</a>
      </div>
    </div>
  </div>
</section>

<section class="projects">
  <div class="wrap">
    <h2 class="section-title">Our Projects</h2>
    <div class="slider-nav">
      <span><svg width="10" height="10" viewBox="0 0 10 10"><path d="M7 1 3 5l4 4" stroke="#888" stroke-width="1.6" fill="none"/></svg></span>
      <span><svg width="10" height="10" viewBox="0 0 10 10"><path d="M3 1l4 4-4 4" stroke="#888" stroke-width="1.6" fill="none"/></svg></span>
    </div>
    <div class="project-list">
      <article class="project">
        <div class="project-photo" role="img" aria-label="Convention center plaza with path lights at dusk" style="background:linear-gradient(180deg,#2a3440 0,#4b5560 45%,#8a6a3a 75%,#3a3228 100%)"></div>
        <h3>Canyon Ridge Expo Center</h3>
        <p>With highly selective LED lighting varieties, we supersede the expectations of our customers and manufacturers with guaranteed.</p>
        <a class="btn" href="#">Read More ›</a>
      </article>
      <article class="project">
        <div class="project-photo" role="img" aria-label="Hotel pool with palm trees lit at night" style="background:linear-gradient(180deg,#0f2550 0,#2b3f74 45%,#2a9ac0 75%,#6fd0e4 100%)"></div>
        <h3>Palm Crest Hotel</h3>
        <p>With highly selective LED lighting varieties, we supersede the expectations of our customers and manufacturers with guaranteed.</p>
        <a class="btn" href="#">Read More ›</a>
      </article>
      <article class="project">
        <div class="project-photo" role="img" aria-label="Modern kitchen interior with blue LED strip lighting" style="background:linear-gradient(180deg,#c9b8a4 0,#a88f78 50%,#6b5fb0 70%,#e8e2da 100%)"></div>
        <h3>Norvale Offices</h3>
        <p>With highly selective LED lighting varieties, we supersede the expectations of our customers and manufacturers with guaranteed.</p>
        <a class="btn" href="#">Read More ›</a>
      </article>
    </div>
  </div>
</section>

<section class="gallery-head">
  <h2 class="section-title">Photo Gallery</h2>
</section>
<div class="gallery">
  <div role="img" aria-label="Garden path lighting outside a house at dusk" style="background:linear-gradient(180deg,#3a4a63,#5a5040)"></div>
  <div role="img" aria-label="Purple lit architectural ceiling" style="background:linear-gradient(180deg,#4a2a80,#1a1a40)"></div>
  <div role="img" aria-label="Dark modern living room interior" style="background:linear-gradient(180deg,#6a6a6a,#2a2a2a)"></div>
  <div role="img" aria-label="Large house exterior lit at twilight" style="background:linear-gradient(180deg,#3a4e8a,#8a7060)"></div>
  <div role="img" aria-label="Close-up of LED bulbs" style="background:linear-gradient(180deg,#b0a8d8,#5a5a8a)"></div>
  <div role="img" aria-label="Blue LED strip on reel" style="background:linear-gradient(180deg,#0a3050,#30a8d8)"></div>
  <div role="img" aria-label="Highway light trails at night" style="background:linear-gradient(180deg,#1a2a6a,#c8d0e8)"></div>
  <div role="img" aria-label="Resort pool lit at night" style="background:linear-gradient(180deg,#2a3a5a,#4a6a7a)"></div>
</div>

<section class="clients">
  <h2 class="section-title">Our Clients</h2>
  <p>We are here to support your needs in energy saving, sustainability, and green building initiatives such as Green Building Design Standard (GBDS) and the Campus Green Rating Program (CGRP).</p>
  <div class="client-row">
    <svg class="client-arrow" viewBox="0 0 24 40"><path d="M18 6 6 20l12 14" stroke="#aaa" stroke-width="3" fill="none"/></svg>
    <div class="client"><span>Altamira Group</span></div>
    <div class="client"><span>Stonefield Build</span></div>
    <div class="client"><span>Arbor Civil</span></div>
    <div class="client"><span>Ridgeline Works</span></div>
    <div class="client"><span>Corvesta</span></div>
    <svg class="client-arrow" viewBox="0 0 24 40"><path d="M6 6l12 14L6 34" stroke="#aaa" stroke-width="3" fill="none"/></svg>
  </div>
</section>

<footer class="site-footer">
  <div class="wrap">
    <div class="footer-cols">
      <div class="footer-col col-links">
        <h4>Quick Links</h4>
        <ul><li>Lighting Investment ROI</li><li>LED Lighting</li><li>Office Lighting</li><li>Lighting Design</li><li>Outdoor Lighting LED</li></ul>
      </div>
      <div class="footer-col col-contact">
        <h4>Contact Info</h4>
        <ul>
          <li>LED Lighting Experts 1480 Sandstone Ave,</li>
          <li>Mesa Verda Texas United States 79000</li>
          <li class="contact-item"><svg width="14" height="14" viewBox="0 0 14 14"><path d="M3 1l2 3-1.5 1.5a8 8 0 0 0 5 5L10 9l3 2-1.5 2.5C6 13 1 8 .5 2.5Z" fill="#fff"/></svg>555 0142 386</li>
          <li class="contact-item"><svg width="14" height="12" viewBox="0 0 14 12"><rect x="0.5" y="0.5" width="13" height="11" fill="#fff"/><path d="M1 1l6 5 6-5" stroke="#f7901e" fill="none"/></svg>info@mesaverdalighting.example</li>
        </ul>
      </div>
      <div class="footer-col">
        <h4>Sign Up for Newsletters</h4>
        <p class="footer-note">Please sign up here for latest news</p>
        <form class="signup"><input type="text" placeholder="EMAIL ADDRESS"><button type="button">Subscribe</button></form>
        <div class="social"><span></span><span></span><span></span><span></span></div>
      </div>
    </div>
    <div class="footer-bottom">© 2017 MESA VERDA LIGHTING &amp; DESIGN . All right reserved . Term of Use</div>
  </div>
</footer>

</body>
</html>
```